Outdoor mass notification company needing business card design.

Our company name is Harborline Signal Systems Inc located in Amory Mississippi and we sell and maintain "Corvath" Mass Notification Sirens in the US. Outdoor sirens notify people of certain severe dangers such as tornados, severe thunderstorms, flooding, hurricanes and tsunamis. We also serve the oil and gas refining industries to warn of Chemical releases, fires, and lightning alerts.

Contact Information for Business Card

Name, title, cell number, email address

Requirements
Nice to have
• The Corvath logo and also the Tallbrook logo.

```html
<!DOCTYPE html>
<html lang="en">
<head>
<meta charset="utf-8">
<title>Harborline Signal Systems Inc – Business Card</title>
<link href="https://fonts.googleapis.com/css2?family=Cinzel:wght@700&family=Montserrat:wght@300;700&display=swap" rel="stylesheet">
<style>
  :root {
    --backdrop: #1e1e1f;
    --card: #36546f;
    --ink: #ffffff;
    --ink-soft: #dfe6ee;
    --siren-dark: #1c1d1f;
    --siren-mid: #4a4d52;
  }
  * { margin: 0; padding: 0; box-sizing: border-box; }
  html, body { width: 1200px; height: 900px; overflow: hidden; }
  body {
    background: var(--backdrop);
    font-family: "Montserrat", sans-serif;
    color: var(--ink);
    display: flex;
    flex-direction: column;
    align-items: center;
    justify-content: center;
    gap: 60px;
  }
  .card {
    position: relative;
    width: 630px;
    height: 360px;
    background: var(--card);
    border-radius: 22px;
    overflow: hidden;
    box-shadow: 0 12px 30px rgba(0,0,0,.45);
  }
  .brand {
    position: absolute;
    display: flex;
    align-items: center;
    gap: 14px;
    font-family: "Cinzel", serif;
    font-weight: 700;
    color: var(--ink);
    line-height: 1.05;
    text-transform: uppercase;
  }
  .brand-dot {
    flex: none;
    border-radius: 50%;
    background: var(--ink);
  }
  .card--front .brand { left: 120px; top: 70px; font-size: 34px; }
  .card--front .brand-dot { width: 18px; height: 18px; }
  .card--back .brand { left: 40px; top: 130px; font-size: 24px; }
  .card--back .brand-dot { width: 13px; height: 13px; }

  .siren-row {
    position: absolute;
    background: linear-gradient(180deg, var(--siren-mid) 0%, var(--siren-dark) 55%, #3b3d40 100%);
    clip-path: polygon(0 0, 100% 55%, 100% 100%, 0 100%);
  }
  .card--front .siren-row { left: 40px; right: 40px; top: 190px; bottom: 0; }
  .card--back .siren-row { left: 315px; right: 0; top: 180px; bottom: 0; }

  .person {
    position: absolute;
    right: 36px;
    top: 34px;
    text-align: right;
  }
  .person-name { font-weight: 700; font-size: 22px; }
  .person-title { font-weight: 300; font-size: 13px; letter-spacing: .06em; color: var(--ink-soft); }

  .contact {
    position: absolute;
    left: 40px;
    bottom: 34px;
    font-weight: 300;
    font-size: 13px;
    color: var(--ink-soft);
  }
  .address { line-height: 1.35; margin-bottom: 14px; }
  .contact-list { list-style: none; }
  .contact-list li { display: flex; align-items: center; gap: 10px; line-height: 1.75; }
  .contact-list svg { width: 13px; height: 13px; fill: var(--ink); flex: none; }
</style>
</head>
<body>
  <section class="card card--front">
    <div class="brand"><span class="brand-dot"></span><span>Harborline Signal<br>Systems Inc</span></div>
    <div class="siren-row" role="img" aria-label="Photo of a row of outdoor warning siren towers"></div>
  </section>

  <section class="card card--back">
    <div class="person">
      <div class="person-name">Dale Whitmore</div>
      <div class="person-title">CEO</div>
    </div>
    <div class="brand"><span class="brand-dot"></span><span>Harborline Signal<br>Systems Inc</span></div>
    <div class="contact">
      <p class="address">418 Main Street, #12<br>Amory, MS 38821</p>
      <ul class="contact-list">
        <li><svg viewBox="0 0 24 24"><path d="M6.6 10.8a15.1 15.1 0 0 0 6.6 6.6l2.2-2.2a1 1 0 0 1 1-.25 11.4 11.4 0 0 0 3.6.57 1 1 0 0 1 1 1V20a1 1 0 0 1-1 1A17 17 0 0 1 3 4a1 1 0 0 1 1-1h3.5a1 1 0 0 1 1 1c0 1.25.2 2.45.57 3.57a1 1 0 0 1-.25 1z"/></svg>662 555-0148</li>
        <li><svg viewBox="0 0 24 24"><path d="M2 5h20v14H2zm2 2v.5l8 5 8-5V7l-8 5z"/></svg>info@harborlinesignal.com</li>
        <li><svg viewBox="0 0 24 24"><path d="M12 2a10 10 0 1 0 0 20 10 10 0 0 0 0-20zm-1 17.9A8 8 0 0 1 4.1 11H7c.1 3.2 1.5 6.3 4 8.9zM7 9H4.1A8 8 0 0 1 11 4.1 12.6 12.6 0 0 0 7 9zm6 10.9c2.5-2.6 3.9-5.7 4-8.9h2.9a8 8 0 0 1-6.9 8.9zM17 9a12.6 12.6 0 0 0-4-4.9A8 8 0 0 1 19.9 9zM9 11h6c-.1 2.6-1.1 5.1-3 7.2-1.9-2.1-2.9-4.6-3-7.2zm0-2c.2-2.4 1.2-4.5 3-6.2 1.8 1.7 2.8 3.8 3 6.2z"/></svg>www.harborlinesignal.com</li>
      </ul>
    </div>
    <div class="siren-row" role="img" aria-label="Photo of a row of outdoor warning siren towers"></div>
  </section>
</body>
</html>
```